Letterhead Design Project

Looking for letterhead designs for Brastova Mining.

I am looking for a letterhead design in conjunction with a business card design. I have opened contests for both but ask that if you submit a letterhead design you also submit a business card design with a corresponding look/feel.

Brastova Mining is a B2B company that buys and sells large machinery tires within the coal mining industry. The design should the strong, crisp and masculine. I have uploaded the company logo and mock-up of the back of the company's business card.

Color scheme should be grey/green/black

Contact information to include:
Name: Dale Whitford
Title: Managing Director
Phone: 555-231-4097
Address: 1817 Pellam #3 Dallas, TX 75290
Email: Dale@Brastova.example
Updates

Project Deadline Extended
Reason: Looking for a more refined, elegant letterhead than what's been submitted as of yet. Here is a sample of what we're looking for: http://www.plumcrestgallery.example/letterhead-designs/ We will also be increasing the payment.

Industry/Entity Type

Coal Mining

```html
<!DOCTYPE html>
<html lang="en">
<head>
<meta charset="utf-8">
<title>Brastova Mining Letterhead</title>
<link href="https://fonts.googleapis.com/css2?family=Arimo:wght@400;700&display=swap" rel="stylesheet">
<style>
  :root {
    --backdrop: #dcdcdc;
    --paper: #ffffff;
    --brand-grey: #6e6e70;
    --band-light: #f4f4f5;
    --band-mid: #d2d2d6;
    --band-dark: #b4b4ba;
    --contact-ink: #6a6a6e;
    --contact-label: #ffffff;
  }
  html, body {
    margin: 0;
    padding: 0;
    width: 1200px;
    height: 1003px;
    overflow: hidden;
    background: var(--backdrop);
    font-family: "Arimo", Arial, sans-serif;
  }
  .letterhead {
    position: absolute;
    left: 262px;
    top: 40px;
    width: 676px;
    height: 922px;
    background: var(--paper);
    box-shadow: 0 4px 18px rgba(0, 0, 0, 0.18);
    overflow: hidden;
  }
  .brand {
    position: absolute;
    top: 58px;
    left: 0;
    right: 0;
    display: flex;
    justify-content: center;
    align-items: center;
    gap: 10px;
  }
  .brand-square {
    width: 22px;
    height: 22px;
    background: var(--brand-grey);
  }
  .brand-name {
    font-weight: 700;
    font-size: 22px;
    letter-spacing: 1.5px;
    color: var(--brand-grey);
    text-transform: uppercase;
  }
  .footer-band {
    position: absolute;
    left: 0;
    bottom: 0;
    width: 676px;
    height: 250px;
  }
  .contact {
    position: absolute;
    left: 150px;
    bottom: 128px;
    font-size: 12px;
    line-height: 16px;
    color: var(--contact-ink);
  }
  .contact-address {
    padding-left: 34px;
  }
  .contact-line span + span {
    margin-left: 14px;
  }
  .contact-label {
    font-weight: 700;
    color: var(--contact-label);
  }
</style>
</head>
<body>
  <main class="letterhead">
    <header class="brand">
      <div class="brand-square"></div>
      <div class="brand-name">Brastova Mining</div>
    </header>

    <svg class="footer-band" viewBox="0 0 676 250" role="img" aria-label="Soft grey dotted halftone band along the foot of the page">
      <defs>
        <linearGradient id="bandFade" x1="0" y1="0" x2="0" y2="1">
          <stop offset="0" stop-color="var(--band-light)" stop-opacity="0"/>
          <stop offset="0.35" stop-color="var(--band-mid)"/>
          <stop offset="1" stop-color="var(--band-dark)"/>
        </linearGradient>
      </defs>
      <path d="M0 20 Q338 -6 676 40 L676 250 L0 250 Z" fill="url(#bandFade)"/>
    </svg>

    <footer class="contact">
      <div class="contact-address">1817 Pellam #3 Dallas, TX 75290</div>
      <div class="contact-line">
        <span><span class="contact-label">Ph:</span> 555-231-4097</span>
        <span><span class="contact-label">E:</span> Dale@Brastova.example</span>
      </div>
    </footer>
  </main>
</body>
</html>
```